velvet shawl

Simple yet classy elegance look
website : www.velvetshawl.co
https://www.facebook.com/velvt.shawl

Attachments are "preferences" I would like to have in similarity

Velvet Shawl presents you the simplest ,classy yet modest suitable for the young and old alike with carefully selected clothing designs and strive to deliver the best customer experience .
To be the leading brand retail fashion at its best and optimizing shopping experience

Target Market(s)

Working ladies , middle to high income earners

Industry/Entity Type

Clothing

Font styles to use
Sans Serif
Decorative
Script

Requirements
Must have
• Simple but eye-catchy
Embossed and alphabetically words engulfed or surround with design

```html
<!DOCTYPE html>
<html lang="en">
<head>
<meta charset="utf-8">
<title>Velvet Shawl — Banner</title>
<link href="https://fonts.googleapis.com/css2?family=Tinos&display=swap" rel="stylesheet">
<style>
  :root {
    --page: #ffffff;
    --violet-deep: #4a2a9e;
    --violet: #6a48c4;
    --periwinkle: #7f86d8;
    --sky: #5a93ea;
    --magenta: #e646c0;
    --rose: #f08ad8;
    --plum: #8a3aa8;
    --ink-light: #ffffff;
  }
  * { margin: 0; padding: 0; box-sizing: border-box; }
  html, body {
    width: 1200px;
    height: 1000px;
    overflow: hidden;
    background: var(--page);
  }
  .canvas {
    position: relative;
    width: 1200px;
    height: 1000px;
    background: var(--page);
  }
  .banner {
    position: absolute;
    left: 212px;
    top: 422px;
    width: 777px;
    height: 155px;
    overflow: hidden;
    background:
      radial-gradient(ellipse 120px 110px at 395px 145px, rgba(255,110,210,0.95), rgba(255,110,210,0) 100%),
      radial-gradient(ellipse 130px 90px at 390px 60px, rgba(240,120,210,0.9), rgba(240,120,210,0) 100%),
      radial-gradient(ellipse 110px 80px at 520px 20px, rgba(90,150,240,0.95), rgba(90,150,240,0) 100%),
      radial-gradient(ellipse 90px 110px at 690px 50px, rgba(225,70,180,0.85), rgba(225,70,180,0) 100%),
      radial-gradient(ellipse 120px 90px at 180px 20px, rgba(130,140,220,0.85), rgba(130,140,220,0) 100%),
      radial-gradient(ellipse 90px 90px at 290px 80px, rgba(180,90,200,0.6), rgba(180,90,200,0) 100%),
      linear-gradient(90deg, var(--violet-deep) 0%, var(--violet) 30%, var(--plum) 50%, var(--violet) 80%, var(--violet-deep) 100%);
  }
  .banner__rule {
    position: absolute;
    left: 228px;
    top: 50px;
    width: 340px;
    height: 3px;
    background: linear-gradient(90deg, rgba(255,255,255,0), rgba(255,255,255,0.9) 30%, rgba(255,255,255,0.95) 60%, rgba(255,255,255,0));
  }
  .banner__name {
    position: absolute;
    left: 0;
    width: 100%;
    top: 43px;
    text-align: center;
    font-family: "Tinos", "Times New Roman", serif;
    font-size: 41px;
    line-height: 1;
    color: var(--ink-light);
  }
  .banner__tagline {
    position: absolute;
    left: 0;
    width: 100%;
    top: 96px;
    text-align: center;
    font-family: "Tinos", "Times New Roman", serif;
    font-size: 21px;
    line-height: 1;
    color: var(--ink-light);
  }
</style>
</head>
<body>
  <main class="canvas">
    <section class="banner">
      <div class="banner__rule"></div>
      <h1 class="banner__name">Velvet Shawl</h1>
      <p class="banner__tagline">Fashion Simplicity</p>
    </section>
  </main>
</body>
</html>
```